Vesta Power Web Design

I want a design for a home page that can function as a template for the entire web design. I"m also requesting that the design be adapted as a template for Power Point presentations, as well.

Here"s a brief about our company:

Vesta Power provides its customers with clean, redundant and reliable power. Functioning as a private power producer, Vesta Power owns and operates combined heat and power (CHP) and distributed generation (DG) systems.

Vesta’s management has extensive experience in aerospace turbines engine operation, maintenance, manufacturing and repair. Depending on the customer need, Vesta either builds new generators or refurbish “retired” aerospace turbines into industrial generators. This allows Vesta to deliver generating systems at greatly reduced capital outlays, enabling Vesta Power to offer its customers not only redundant power and grid independence, but significant savings on their energy needs. Vesta’s typical installation size is 500Kws to 3Mws but based upon our customer"s needs, Vesta can site multiple generators to configure systems of larger size.

By using aero derivative turbine engines the company has the flexibility to use the best source of fuel for each site and power requirement. The turbine engine can operate on virtually any combustible fuel. This allows Vesta to utilize the flex fuel practice and operate on either the least expensive fuel available or operate on renewable and biofuels to fulfill the green power requirements mandated by many federal, state and local utility commissions.

Vesta’s market strategy is as follows:

1. Sell reliable and redundant power through a PPAs or lease agreements to industrial or institutional customers with high electrical and thermal needs such as food processors, bio fuel producers, hospitals, casinos, hotels, etc.

2. Lease its systems to customer that “flare gas” as byproducts of their processes such as wastewater treatment facilities, land fills and "stranded gas wells" allowing them to use their waste products to power their facilities and sell excess electricity back to the grid.

3. Partner with other private power producers to provide the turbine generating capacity on a leased basis.
Updates

Please disregard the "turbine logo" that was uploaded as a file and focus only on the "bolt design logo", A (bolt) E.

We like the simple navigation and clean and modern design of sites.

http://www.plumvault.example/

http://www.serviqo.example/

http://www.trylumo.example/

Target Market(s)

Our target markets can be found on the web architecture file I've attached to this submission.

Number of Pages Required

1 page

Requirements
Must have
• The designer must provide a web design and a Power Point template based upon the web design.

• The design must contemplate the web architecture that I""ve included as a file.

```html
<!DOCTYPE html>
<html lang="en">
<head>
<meta charset="utf-8">
<title>Vesta Power</title>
<link href="https://fonts.googleapis.com/css2?family=Open+Sans:wght@300;400;600;700&family=PT+Sans:wght@400;700&display=swap" rel="stylesheet">
<style>
  :root {
    --brand-green: #1f6a24;
    --brand-deep: #0f4a18;
    --button-top: #6fb53a;
    --button-bottom: #0d5b1d;
    --text-dark: #1d1d1d;
    --text-body: #222;
    --panel-fill: rgba(236, 232, 212, 0.78);
    --panel-border: rgba(255, 255, 255, 0.8);
    --frame: #8ea77c;
    --bg-top: #bfd79a;
    --bg-mid: #dfe8c4;
    --bg-bottom: #f2efe6;
    --link: #1f6a24;
  }
  * { margin: 0; padding: 0; box-sizing: border-box; }
  html, body { width: 1200px; height: 1058px; overflow: hidden; }
  body {
    position: relative;
    background: linear-gradient(180deg, var(--bg-top) 0%, var(--bg-mid) 40%, var(--bg-bottom) 75%, var(--bg-bottom) 100%);
    font-family: "Open Sans", sans-serif;
    color: var(--text-body);
  }
  .brand {
    position: absolute; left: 53px; top: 0; width: 239px; height: 187px;
    background: var(--brand-green);
    border: 1px solid #7fa66a; border-top: none;
    display: flex; flex-direction: column; align-items: center; justify-content: center; gap: 14px;
  }
  .brand-dot { width: 54px; height: 54px; border-radius: 50%; background: #c8dc4c; }
  .brand-name { font-family: "Open Sans", sans-serif; font-weight: 400; font-size: 28px; color: #fff; }
  .main-nav {
    position: absolute; left: 349px; top: 36px; width: 836px;
    display: flex; justify-content: space-between;
  }
  .main-nav a {
    font-family: "Open Sans", sans-serif; font-weight: 300; font-size: 21px; letter-spacing: -0.4px;
    color: var(--text-dark); text-decoration: none;
  }
  .welcome {
    position: absolute; left: 14px; top: 196px;
    font-family: "Open Sans", sans-serif; font-weight: 300; font-size: 21px; color: var(--text-dark);
  }
  .welcome span { font-size: 36px; color: #fff; letter-spacing: -0.5px; }
  .intro {
    position: absolute; left: 14px; top: 252px; width: 485px;
    font-size: 14px; line-height: 22px; color: var(--text-body);
  }
  .intro p + p { margin-top: 21px; }
  .read-more {
    position: absolute; left: 7px; top: 434px; width: 85px; height: 22px;
    background: var(--brand-deep); border: 1px solid #e8eed8;
    color: #fff; font-size: 12px; line-height: 20px; text-align: center; text-decoration: none;
  }
  .hero-frame {
    position: absolute; left: 521px; top: 101px; width: 663px; height: 355px;
    background: var(--frame); border: 1px solid #6f8c5c;
  }
  .hero-photo {
    position: absolute; left: 14px; top: 13px; width: 635px; height: 329px;
    background: linear-gradient(160deg, #b4c7d6 0%, #6e8ea8 35%, #3f5f82 60%, #9aa8ad 100%);
  }
  .panel {
    position: absolute; top: 498px; height: 283px;
    background: var(--panel-fill); border: 2px solid var(--panel-border); border-radius: 14px;
  }
  .panel h2 {
    font-family: "Open Sans", sans-serif; font-weight: 400; font-size: 20px; color: var(--text-dark);
    letter-spacing: -0.3px;
  }
  .strategy { left: 6px; width: 741px; padding: 10px 18px; }
  .strategy ol { list-style: none; margin-top: 16px; font-size: 13.8px; line-height: 21.5px; }
  .strategy li + li { margin-top: 21px; }
  .strategy b { font-weight: 700; }
  .contact { left: 790px; width: 394px; padding: 10px 30px; overflow: hidden; }
  .contact address {
    font-style: normal; font-family: "PT Sans", sans-serif; font-weight: 700; font-size: 15px; line-height: 21.5px;
    margin-top: 8px; color: #111;
  }
  .contact dl { margin-top: 16px; font-size: 14px; line-height: 22px; }
  .contact dt { display: inline; font-weight: 700; }
  .contact dd { display: inline; }
  .mailbox-art {
    position: absolute; right: 0; top: 56px; width: 100px; height: 192px;
    background: linear-gradient(180deg, #d9d4c2 0%, #bdb8aa 60%, rgba(200,195,180,0) 100%);
  }
  .cta {
    position: absolute; top: 825px; width: 364px; height: 121px;
    border-radius: 14px; border: 2px solid #e8eedc;
    background: linear-gradient(180deg, var(--button-top) 0%, #3c8a2b 45%, var(--button-bottom) 100%);
    display: flex; align-items: center; justify-content: center; text-align: center;
    font-family: "Open Sans", sans-serif; font-weight: 400; font-size: 26px; line-height: 29px;
    color: #fff; text-decoration: none; letter-spacing: -0.6px;
  }
  .cta-law { left: 8px; }
  .cta-fit { left: 413px; }
  .cta-calc { left: 818px; }
  .site-footer {
    position: absolute; left: 0; top: 988px; width: 1200px; text-align: center;
    font-size: 12.5px; line-height: 18px; color: var(--text-dark);
  }
  .site-footer a { color: var(--link); text-decoration: none; }
  .site-footer .sep { margin: 0 11px; }
</style>
</head>
<body>
  <header>
    <div class="brand">
      <span class="brand-dot"></span>
      <span class="brand-name">Vesta Power</span>
    </div>
    <nav class="main-nav">
      <a href="#">Home</a><a href="#">About Vesta</a><a href="#">CHP</a><a href="#">Stranded Gas</a><a href="#">Resources</a><a href="#">Partners &amp; Suppliers</a><a href="#">Contact Us</a>
    </nav>
  </header>

  <h1 class="welcome">welcome to <span>vesta power</span></h1>
  <div class="intro">
    <p>Vesta Power provides its customers with clean, redundant and reliable power. Functioning as a private power producer, Vesta Power owns and operates combined heat and power (CHP) and distributed generation (DG) systems.</p>
    <p>Vesta’s management has extensive experience in aerospace turbines engine operation, maintenance, manufacturing and repair. Depending on the customer need, Vesta either builds new generators or refurbish.....</p>
  </div>
  <a class="read-more" href="#">read more..</a>

  <div class="hero-frame">
    <div class="hero-photo" role="img" aria-label="Photograph of a power plant hall with pipes, turbines and blue steel frames"></div>
  </div>

  <section class="panel strategy">
    <h2>Our Marketing Strategy</h2>
    <ol>
      <li><b>1.</b> Sell reliable and redundant power through a PPAs or lease agreements to industrial or institutional customers with high electrical and thermal needs such as food processors, bio fuel producers, hospitals, casinos, hotels, etc.</li>
      <li><b>2.</b> Lease its systems to customer that “flare gas” as byproducts of their processes such as wastewater treatment facilities, land fills and "stranded gas wells" allowing them to use their waste products to power their facilities and sell excess electricity back to the grid.</li>
      <li><b>3.</b> Partner with other private power producers to provide the turbine generating capacity on a leased basis.</li>
    </ol>
  </section>

  <section class="panel contact">
    <h2>Contact Details</h2>
    <address>10th Apartment,<br>5th Floor,<br>Elmwood Street,<br>Country Name</address>
    <dl>
      <dt>Phone:</dt> <dd>55510 55510,5551055512</dd><br>
      <dt>Fax:</dt> <dd>33 55510 55510</dd><br>
      <dt>Email :</dt> <dd>support@vestapower.example</dd>
    </dl>
    <div class="mailbox-art" role="img" aria-label="Illustration of a mailbox stuffed with letters"></div>
  </section>

  <a class="cta cta-law" href="#">Texas CHP Critical<br>Infrastructure Legislation</a>
  <a class="cta cta-fit" href="#">Is your Business a Good<br>Candidate For CHP</a>
  <a class="cta cta-calc" href="#">CHP Calculator</a>

  <footer class="site-footer">
    <div>
      <a href="#">Home</a><span class="sep">|</span><a href="#">About Vesta</a><span class="sep">|</span><a href="#">CHP</a><span class="sep">|</span><a href="#">Staranded Gas</a><span class="sep">|</span><a href="#">Resources</a><span class="sep">|</span><a href="#">Partners &amp; Suppliers</a><span class="sep">|</span><a href="#">Contact Us</a>
    </div>
    <div>© 2010-2011 | &nbsp;All Rights Reserved</div>
  </footer>
</body>
</html>
```